Brova Equipment Sales & Rentals

We are an independent equipment dealership located in the upstate of South Carolina. Our services include Equipment Sales, Equipment Rentals, Metal Sales, and Industrial Supplies.

I have attached our logos and a few billboards that we like as examples for inspiration. Thank you!

Phone Number 864-555-0172

Website link if you want to check out our page.
https://www.brovaequip.example

```html
<!DOCTYPE html>
<html lang="en">
<head>
<meta charset="utf-8">
<title>Brova Equipment Sales &amp; Rentals – Billboard</title>
<link href="https://fonts.googleapis.com/css2?family=Saira:ital,wght@0,800;0,900;1,800&display=swap" rel="stylesheet">
<style>
  :root {
    --page: #ececec;
    --sky-deep: #5aa8e8;
    --sky-light: #d8ecfb;
    --red: #e3151b;
    --red-dark: #9e0d10;
    --ink: #0c0c0c;
    --white: #ffffff;
    --machine: #c9962f;
    --haze: #f3e6d2;
  }
  * { margin: 0; padding: 0; box-sizing: border-box; }
  html, body { width: 976px; height: 1200px; overflow: hidden; background: var(--page); }
  body { position: relative; font-family: "Saira", "Arial Narrow", sans-serif; }

  .billboard {
    position: absolute; left: 38px; top: 375px; width: 900px; height: 450px;
    overflow: hidden;
    background: linear-gradient(180deg, var(--sky-deep) 0%, #8cc4f0 45%, var(--sky-light) 100%);
    box-shadow: 0 14px 30px rgba(0,0,0,.28);
  }
  .photo-area {
    position: absolute; right: 0; top: 0; width: 600px; height: 377px;
    background:
      linear-gradient(90deg, rgba(190,222,247,1) 0%, rgba(216,236,251,.85) 22%, rgba(216,236,251,0) 50%),
      linear-gradient(180deg, #8fa6bb 0%, var(--haze) 45%, var(--machine) 78%, #8a6a3a 100%);
  }

  .brand {
    position: absolute; left: 49px; top: 42px;
    display: flex; align-items: center; gap: 16px;
  }
  .brand-mark { width: 44px; height: 44px; background: var(--red); }
  .brand-name { font-weight: 900; font-size: 76px; line-height: 1; color: var(--ink); letter-spacing: 1px; }

  .service { position: absolute; display: flex; align-items: center; gap: 14px; }
  .service-icon { width: 50px; height: 54px; flex: none; }
  .service-label {
    font-weight: 800; font-style: italic; font-size: 21px; line-height: 1.15; color: var(--ink);
  }
  .s1 { left: 49px; top: 160px; }
  .s2 { left: 252px; top: 160px; }
  .s3 { left: 49px; top: 250px; }
  .s4 { left: 252px; top: 250px; }

  .contact-bar { position: absolute; left: 0; bottom: 0; width: 900px; height: 73px; }
  .contact-bar > .bar-shape { position: absolute; inset: 0; width: 900px; height: 73px; }
  .website {
    position: absolute; left: 50px; top: 0; height: 73px;
    display: flex; align-items: center; gap: 12px;
    font-weight: 800; font-style: italic; font-size: 26px; line-height: 1; color: var(--white);
  }
  .website .domain { color: var(--red); }
  .phone {
    position: absolute; left: 472px; top: 0; height: 73px;
    display: flex; align-items: center; gap: 18px;
    font-weight: 800; font-style: italic; font-size: 42px; line-height: 1; color: var(--ink); letter-spacing: 1px;
  }
  .bar-icon { flex: none; }
</style>
</head>
<body>
  <section class="billboard" aria-label="Brova Equipment Sales and Rentals billboard">
    <div class="photo-area" role="img" aria-label="Photo of yellow excavators and a bulldozer on a dirt lot under a bright cloudy sky"></div>

    <div class="brand">
      <span class="brand-mark"></span>
      <span class="brand-name">BROVA</span>
    </div>

    <div class="service s1">
      <svg class="service-icon" viewBox="0 0 50 54" aria-hidden="true"><polygon points="25,2 47,14 47,40 25,52 3,40 3,14" fill="var(--red)" stroke="var(--red-dark)" stroke-width="3"/><g fill="none" stroke="#fff" stroke-width="2"><rect x="14" y="30" width="22" height="7" rx="3"/><path d="M18 30v-7h8v7M26 26l6-10 4 6"/></g></svg>
      <span class="service-label">Equipment<br>Sales</span>
    </div>
    <div class="service s2">
      <svg class="service-icon" viewBox="0 0 50 54" aria-hidden="true"><polygon points="25,2 47,14 47,40 25,52 3,40 3,14" fill="var(--red)" stroke="var(--red-dark)" stroke-width="3"/><g fill="none" stroke="#fff" stroke-width="2"><path d="M14 34l14-16h8l-14 16z M20 27l8 0"/></g></svg>
      <span class="service-label">Metal<br>Sales</span>
    </div>
    <div class="service s3">
      <svg class="service-icon" viewBox="0 0 50 54" aria-hidden="true"><polygon points="25,2 47,14 47,40 25,52 3,40 3,14" fill="var(--red)" stroke="var(--red-dark)" stroke-width="3"/><g fill="none" stroke="#fff" stroke-width="2"><rect x="13" y="31" width="24" height="7" rx="3"/><path d="M17 31v-8h10v8M17 23l-2-8 6 3"/></g></svg>
      <span class="service-label">Equipment<br>Rentals</span>
    </div>
    <div class="service s4">
      <svg class="service-icon" viewBox="0 0 50 54" aria-hidden="true"><polygon points="25,2 47,14 47,40 25,52 3,40 3,14" fill="var(--red)" stroke="var(--red-dark)" stroke-width="3"/><g fill="none" stroke="#fff" stroke-width="2"><rect x="13" y="24" width="12" height="12"/><rect x="27" y="18" width="8" height="12"/><path d="M25 36h12"/></g></svg>
      <span class="service-label">Industrial<br>Supplies</span>
    </div>

    <div class="contact-bar">
      <svg class="bar-shape" viewBox="0 0 900 73" preserveAspectRatio="none" aria-hidden="true">
        <rect width="900" height="73" fill="var(--white)"/>
        <polygon points="0,0 440,0 468,73 0,73" fill="var(--ink)"/>
        <polygon points="0,0 40,73 0,73" fill="var(--red)"/>
        <polygon points="860,0 900,0 900,73" fill="var(--red)"/>
      </svg>
      <div class="website">
        <svg class="bar-icon" width="28" height="28" viewBox="0 0 26 26" aria-hidden="true"><g fill="none" stroke="var(--red)" stroke-width="2"><circle cx="13" cy="13" r="11"/><ellipse cx="13" cy="13" rx="5" ry="11"/><path d="M2 13h22M4 7h18M4 19h18"/></g></svg>
        <span>www.<span class="domain">brovaequip</span>.example</span>
      </div>
      <div class="phone">
        <svg class="bar-icon" width="30" height="30" viewBox="0 0 24 24" aria-hidden="true"><path fill="var(--red)" d="M6.6 10.8a15 15 0 0 0 6.6 6.6l2.2-2.2a1 1 0 0 1 1-.25 11 11 0 0 0 3.6.6 1 1 0 0 1 1 1V20a1 1 0 0 1-1 1A17 17 0 0 1 3 4a1 1 0 0 1 1-1h3.5a1 1 0 0 1 1 1c0 1.25.2 2.45.6 3.6a1 1 0 0 1-.25 1z"/></svg>
        <span>864-555-0172</span>
      </div>
    </div>
  </section>
</body>
</html>
```